High end Electrical/home automation Business Card

Need a card for a high end electrical and home automation company utilising the existing logo.
Phone
Email
Website

Like black look with raised detail. Don’t necessarily need to keep colour of logo it could be made grayscale or white etc

Target Market(s)

High end clients

Contact Information for Business Card

Northwell Electrical

Requirements
Must have
• Logo, phone, email, website, address

High end look
Nice to have
• Black background card
Raised font
Should not have
• Lots of colour

```html
<!DOCTYPE html>
<html lang="en">
<head>
<meta charset="utf-8">
<title>Northwell Electrical – Business Card</title>
<link href="https://fonts.googleapis.com/css2?family=Archivo:wght@800&family=Lato:wght@300;400;700;900&display=swap" rel="stylesheet">
<style>
  :root {
    --page-bg: #2b2c2f;
    --card-front: #3a3a3d;
    --card-back: #303033;
    --pattern-dark: #262628;
    --pattern-light: #3b3b3e;
    --accent: #2393d6;
    --ink: #ffffff;
    --ink-soft: #e6e6e6;
  }
  * { box-sizing: border-box; margin: 0; padding: 0; }
  html, body { width: 1200px; height: 900px; overflow: hidden; }
  body {
    background: var(--page-bg);
    font-family: "Lato", sans-serif;
    position: relative;
  }
  .card {
    position: absolute;
    left: 250px;
    width: 700px;
    height: 400px;
    border-radius: 30px;
    overflow: hidden;
  }
  /* Back side */
  .card-back { top: 30px; background: var(--card-back); }
  .back-pattern {
    position: absolute; inset: 0;
    background: linear-gradient(100deg, var(--pattern-light) 0%, var(--pattern-dark) 60%, #1f1f21 100%);
  }
  .back-mark {
    position: absolute; left: 440px; top: 200px;
    display: flex; align-items: center; gap: 8px;
    font-family: "Archivo", sans-serif; font-weight: 800;
    font-size: 18px; color: var(--accent);
  }
  .back-mark .dot { width: 12px; height: 12px; border-radius: 50%; background: var(--accent); }

  /* Front side */
  .card-front { top: 470px; background: var(--card-front); }
  .brand {
    position: absolute; left: 48px; top: 80px;
    font-family: "Archivo", sans-serif; font-weight: 800;
    font-size: 40px; letter-spacing: -1px; color: var(--ink);
  }
  .brand .brand-accent { color: var(--accent); }
  .person { position: absolute; left: 110px; top: 160px; }
  .person-name {
    font-weight: 900; font-size: 34px; letter-spacing: 0.5px; color: var(--ink);
  }
  .person-name .surname { color: var(--accent); }
  .person-role { font-weight: 300; font-size: 19px; color: var(--ink-soft); margin-top: 2px; }
  .address { margin-top: 14px; font-weight: 300; font-size: 18px; line-height: 1.3; color: var(--ink-soft); }
  .contact { margin-top: 14px; list-style: none; }
  .contact li {
    display: flex; align-items: center; gap: 12px;
    font-weight: 300; font-size: 18px; line-height: 1.5; color: var(--ink-soft);
  }
  .contact svg { width: 18px; height: 18px; flex: none; }
  .front-mark {
    position: absolute; left: 440px; top: 40px;
    width: 240px; height: 240px;
    border: 22px solid var(--accent); border-radius: 50%;
    display: flex; align-items: center; justify-content: center; text-align: center;
    font-family: "Archivo", sans-serif; font-weight: 800;
    font-size: 26px; line-height: 1.1; color: var(--ink);
  }
</style>
</head>
<body>
  <section class="card card-back" aria-label="Card back">
    <div class="back-pattern" role="img" aria-label="Repeating tone-on-tone company mark pattern"></div>
    <div class="back-mark"><span class="dot"></span>Northwell Electrical</div>
  </section>

  <section class="card card-front" aria-label="Card front">
    <h1 class="brand">Northwell <span class="brand-accent">Electrical</span></h1>
    <div class="person">
      <p class="person-name">DANIEL <span class="surname">HART</span></p>
      <p class="person-role">Founder &amp; CEO</p>
      <p class="address">1234 First Line Address<br>5678 Second Line Address</p>
      <ul class="contact">
        <li>
          <svg viewBox="0 0 24 24" aria-hidden="true"><path fill="var(--accent)" d="M6.6 10.8a15.1 15.1 0 0 0 6.6 6.6l2.2-2.2c.3-.3.7-.4 1-.2 1.1.4 2.3.6 3.6.6.6 0 1 .4 1 1V20c0 .6-.4 1-1 1A17 17 0 0 1 3 4c0-.6.4-1 1-1h3.5c.6 0 1 .4 1 1 0 1.3.2 2.5.6 3.6.1.3 0 .7-.2 1z"/></svg>
          1234567890
        </li>
        <li>
          <svg viewBox="0 0 24 24" aria-hidden="true"><rect x="2" y="5" width="20" height="14" rx="1" fill="var(--accent)"/><path d="M2 6l10 7 10-7" fill="none" stroke="var(--card-front)" stroke-width="1.6"/></svg>
          info@yourmail.com
        </li>
        <li>
          <svg viewBox="0 0 24 24" aria-hidden="true"><g fill="none" stroke="var(--accent)" stroke-width="1.8"><circle cx="12" cy="12" r="9"/><ellipse cx="12" cy="12" rx="4" ry="9"/><path d="M3 12h18"/></g></svg>
          www.yourwebsite.com
        </li>
      </ul>
    </div>
    <div class="front-mark">Northwell<br>Electrical</div>
  </section>
</body>
</html>
```